Floral Waters needs a Label Design for bottles

Our products slogan: grown with water and sun.
Organic products of excellence originating from regions of extraordinary environmental quality, these products are the basis of natural cosmetics. Bio certificated and Organic.

We need a Luxury Label for the bottles of Floral Waters.
We don't want rustic, organic, rural, bio...
We want Luxury associated with environment.

The Label / decoration for the bottles must be editable, for we can change the titles of the floral Waters and information.
Elements :
Floral Water
Pet and Glass round Bottles Dimensions: 11cm Height , 4.5cm width
perimeter - 7.65
The logo is from tv lumora web store, it´s not necessary to include in the front of the paching design. it´s an open option

Target Market(s)

Medium High urban people , with ecologic and sustainable concerns. People who prefer natural and non Quimical cosmetics.

Industry/Entity Type

Floral

Requirements
Must have
• Sophisticated simple design
• Elements :
• Floral Water
• space for the name of the Floral Water ( ex: Salvia Officinalis, Minth, Melissa Officinalis)
• Grown with water and sun
Nice to have
• Variations of Gold
Should not have
• Bio, farm, organic, rustic,

```html
<!DOCTYPE html>
<html lang="en">
<head>
<meta charset="utf-8">
<title>Floral Water Label – Salvia Officinalis</title>
<link rel="stylesheet" href="https://fonts.googleapis.com/css2?family=Cinzel:wght@400;600&family=EB+Garamond:wght@400;500&family=Sorts+Mill+Goudy&display=swap">
<style>
  :root {
    --backdrop: #ededed;
    --label-white: #ffffff;
    --leaf-green: #1f7a3a;
    --deep-green: #1d4a2a;
    --ink: #2b2b2b;
    --gold: #a07a1e;
    --ornament-light: #d9ebdd;
    --ornament-mid: #4f9a62;
  }
  html, body {
    margin: 0;
    padding: 0;
    width: 1035px;
    height: 1200px;
    overflow: hidden;
    background: var(--backdrop);
  }
  .canvas {
    position: relative;
    width: 1035px;
    height: 1200px;
  }
  .label {
    position: absolute;
    left: 297px;
    top: 90px;
    width: 440px;
    height: 1020px;
    background: var(--label-white);
    box-shadow: 0 2px 10px rgba(0,0,0,0.08);
    display: flex;
    flex-direction: column;
    align-items: center;
    box-sizing: border-box;
  }
  .ornament {
    width: 100%;
    height: 230px;
    flex: none;
  }
  .ornament--top {
    background: linear-gradient(180deg, var(--ornament-mid) 0%, var(--ornament-light) 100%);
  }
  .ornament--bottom {
    margin-top: auto;
    background: linear-gradient(0deg, var(--ornament-mid) 0%, var(--ornament-light) 100%);
  }
  .brand {
    margin-top: 70px;
    display: flex;
    align-items: center;
    gap: 10px;
    font-family: "EB Garamond", serif;
    font-weight: 500;
    font-size: 26px;
    color: var(--gold);
    letter-spacing: 0.5px;
  }
  .brand-dot {
    width: 12px;
    height: 12px;
    border-radius: 50%;
    background: var(--gold);
  }
  .title-block {
    margin-top: 30px;
    width: 360px;
    text-align: center;
  }
  .rule {
    display: block;
    width: 100%;
    height: 10px;
  }
  .title {
    margin: 6px 0 4px;
    font-family: "Sorts Mill Goudy", serif;
    font-weight: 400;
    font-size: 60px;
    line-height: 1.05;
    color: var(--deep-green);
  }
  .tagline {
    margin: 22px 0 0;
    font-family: "Cinzel", serif;
    font-size: 14px;
    letter-spacing: 1.5px;
    color: var(--ink);
  }
  .variety {
    margin-top: 22px;
    width: 300px;
    padding: 14px 0;
    border: 1.5px solid var(--deep-green);
    border-radius: 26px;
    text-align: center;
    font-family: "Cinzel", serif;
    font-weight: 600;
    font-size: 19px;
    letter-spacing: 0.5px;
    color: var(--deep-green);
    box-shadow: inset 0 0 0 4px var(--label-white), inset 0 0 0 5px var(--deep-green);
  }
  .description {
    margin: 26px 0 0;
    width: 340px;
    font-family: "EB Garamond", serif;
    font-size: 13px;
    line-height: 1.3;
    text-align: justify;
    color: var(--ink);
  }
</style>
</head>
<body>
<main class="canvas">
  <section class="label">
    <div class="ornament ornament--top" role="img" aria-label="Green floral scrollwork ornament with leaves and vines"></div>

    <div class="brand"><span class="brand-dot"></span>tv lumora</div>

    <div class="title-block">
      <svg class="rule" viewBox="0 0 360 10" preserveAspectRatio="none" aria-hidden="true">
        <line x1="0" y1="5" x2="360" y2="5" stroke="#1d4a2a" stroke-width="1.5"/>
      </svg>
      <h1 class="title">Floral Water</h1>
      <svg class="rule" viewBox="0 0 360 10" preserveAspectRatio="none" aria-hidden="true">
        <line x1="0" y1="5" x2="360" y2="5" stroke="#1d4a2a" stroke-width="1.5"/>
      </svg>
      <p class="tagline">GROWN WITH WATER AND SUN</p>
    </div>

    <div class="variety">SALVIA OFFICINALIS</div>

    <p class="description">Pure sage water distilled slowly from fresh leaves picked at dawn in clean mountain valleys. Gently tones, calms and refreshes the skin while keeping its natural balance. Shake well before use and mist lightly over face and neck. Store away from direct light and heat. Use within six months after opening for best results every day.</p>

    <div class="ornament ornament--bottom" role="img" aria-label="Green floral scrollwork ornament with leaves and vines"></div>
  </section>
</main>
</body>
</html>
```